Vesk Architecture

We are a architectural design and build company working between scales 1/1000 to 1/1 we want people to understand our difference from our design experience and quality.we build hotels restourants and office spaces.Our company name is Vesk architecture to mind sustainability.

We want to write our adress phone and work spesifications on the card and we want our logo as backround.

Ps:you could find the logo adress and phone box numbers from the web:www.veskmimarlik-ornek.com

Target Market(s)

Who looks for experts.

Industry/Entity Type

Architecture

Requirements
Must have
• Design is over everything.
Should not have
• we don want it to be colorfull

```html
<!DOCTYPE html>
<html lang="en">
<head>
<meta charset="utf-8">
<title>Vesk Architecture – Business Card</title>
<link rel="stylesheet" href="https://fonts.googleapis.com/css2?family=Arimo:wght@400;700&family=Poppins:wght@400&display=swap">
<style>
  :root {
    --page: #ffffff;
    --ink: #000000;
    --paper-light: #f4f4f4;
    --paper-mid: #d9d9d9;
    --paper-dark: #b8b8b8;
    --rule: #111111;
    --dash: #333333;
    --faint: #9a9a9a;
    --reverse: #ffffff;
  }
  html, body {
    margin: 0;
    padding: 0;
    width: 1200px;
    height: 458px;
    overflow: hidden;
    background: var(--page);
  }
  .sheet { display: block; width: 1200px; height: 458px; }
  .wordmark { font-family: "Poppins", Arial, sans-serif; font-weight: 400; fill: var(--ink); }
  .descriptor { font-family: "Arimo", Arial, sans-serif; font-weight: 700; fill: var(--ink); letter-spacing: 0.5px; }
  .contact { font-family: "Arimo", Arial, sans-serif; font-weight: 400; fill: var(--ink); }
  .contact-strong { font-family: "Arimo", Arial, sans-serif; font-weight: 700; fill: var(--ink); }
  .web-address { font-family: "Arimo", Arial, sans-serif; font-weight: 400; fill: var(--reverse); }
  .side-label { font-family: "Arimo", Arial, sans-serif; font-weight: 700; fill: var(--ink); }
  .guide { stroke: var(--rule); stroke-width: 1; fill: none; }
  .guide-dashed { stroke: var(--dash); stroke-width: 1; stroke-dasharray: 5 4; fill: none; }
  .band { fill: var(--ink); }
  .backdrop-name { font-family: "Poppins", Arial, sans-serif; font-weight: 400; fill: var(--faint); opacity: 0.35; }
</style>
</head>
<body>
<svg class="sheet" viewBox="0 0 817 311.8" preserveAspectRatio="none" role="img" aria-label="Vesk Architecture business card, front and back">
  <defs>
    <linearGradient id="paper-front" x1="0" y1="0" x2="1" y2="0">
      <stop offset="0" stop-color="var(--paper-mid)"/>
      <stop offset="0.35" stop-color="var(--paper-light)"/>
      <stop offset="0.7" stop-color="var(--paper-light)"/>
      <stop offset="1" stop-color="var(--paper-dark)"/>
    </linearGradient>
    <linearGradient id="paper-back" x1="0" y1="0" x2="1" y2="0">
      <stop offset="0" stop-color="var(--paper-mid)"/>
      <stop offset="0.45" stop-color="var(--paper-light)"/>
      <stop offset="1" stop-color="var(--paper-dark)"/>
    </linearGradient>
  </defs>

  <!-- Front side -->
  <g class="card card-front">
    <rect x="0" y="0" width="400" height="283" fill="url(#paper-front)"/>
    <polygon points="0,0 14,0 0,22" fill="var(--ink)" opacity="0.75"/>
    <line class="guide" x1="93" y1="0" x2="93" y2="80"/>
    <line class="guide" x1="297" y1="0" x2="297" y2="80"/>
    <line class="guide" x1="297" y1="40" x2="400" y2="40"/>
    <line class="guide" x1="0" y1="80" x2="400" y2="80"/>
    <line class="guide" x1="105" y1="82" x2="400" y2="82"/>
    <line class="guide" x1="105" y1="82" x2="105" y2="155"/>
    <line class="guide" x1="0" y1="155" x2="232" y2="155"/>
    <line class="guide-dashed" x1="110" y1="101" x2="340" y2="101"/>
    <line class="guide-dashed" x1="255" y1="197" x2="335" y2="197"/>
    <line class="guide-dashed" x1="110" y1="160" x2="110" y2="236"/>

    <text class="wordmark" x="112" y="152" font-size="78">vesk</text>
    <text class="descriptor" x="147" y="177" font-size="12">MİMARLIK</text>

    <rect class="band" x="0" y="275" width="400" height="8"/>
    <polygon class="band" points="248,261 400,261 400,283 238,283"/>
    <text class="web-address" x="394" y="277" font-size="12" text-anchor="end">www.veskmimarlik-ornek.com</text>
  </g>
  <text class="side-label" x="163" y="302" font-size="7">FRONT SIDE</text>

  <!-- Back side -->
  <g class="card card-back" transform="translate(418 0)">
    <rect x="0" y="0" width="399" height="283" fill="url(#paper-back)"/>
    <text class="backdrop-name" x="395" y="262" font-size="110" text-anchor="end">vesk</text>

    <text class="wordmark" x="199" y="50" font-size="46" text-anchor="middle">vesk</text>
    <line class="guide" x1="0" y1="62" x2="122" y2="62"/>
    <line class="guide" x1="122" y1="55" x2="122" y2="69"/>
    <line class="guide" x1="277" y1="62" x2="399" y2="62"/>
    <line class="guide" x1="277" y1="55" x2="277" y2="69"/>

    <text class="contact" x="199" y="106" font-size="8.5" text-anchor="middle">Kestane Mah, Liman Cad, Ayva Sok</text>
    <text class="contact" x="199" y="119" font-size="8.5" text-anchor="middle">No : 7 Yelken Kadikoy/Istanbul</text>

    <text class="contact-strong" x="146" y="159" font-size="12.5">T :0216 555 0142</text>
    <text class="contact-strong" x="146" y="175" font-size="12.5">F :0216 555 01 87</text>
    <text class="contact" x="126" y="186" font-size="8.5">Email : veskmimarlik@ornek-posta.com</text>

    <rect class="band" x="0" y="266" width="399" height="17"/>
  </g>
  <text class="side-label" x="626" y="299" font-size="7" text-anchor="middle">BACK SIDE</text>
</svg>
</body>
</html>
```